CRPG is needing business cards, and stationary created.

Pixel Forge created a logo for our business, and now we are wanting business cards, and stationary. I have included two designs of the same logo. Please feel free to use them as you want. The name of the company is Cedar Ridge Property Group LLC, the address is 812 NE Tamber Ln., Suite 9, the city & state is Alderton, Nevada, zip code is 97815, Telephone number is 555-237-4190, Fax number is 555-237-8856, the name on the business card is Travis Lundqor CMCA

Industry/Entity Type

Property Management

Contact Information for Business Card

The card needs to look professional. Upscale.

Requirements
Must have
• The colors we are using are on the logo that has been uploaded.

```html
<!DOCTYPE html>
<html lang="en">
<head>
<meta charset="utf-8">
<title>Cedar Ridge Property Group – Stationery</title>
<link href="https://fonts.googleapis.com/css2?family=Arimo:wght@400;700&family=Lato:wght@400;700;900&display=swap" rel="stylesheet">
<style>
  :root {
    --teal: #1a8a76;
    --slate: #3a4a5a;
    --paper: #f4f4f4;
    --ink: #6b6b6b;
    --backdrop: #d9d6d2;
    --signature: #dcdcdc;
  }
  * { margin: 0; padding: 0; box-sizing: border-box; }
  html, body { width: 1200px; height: 1200px; overflow: hidden; }
  body { background: var(--backdrop); position: relative; font-family: "Arimo", Arial, sans-serif; }

  .card { position: absolute; left: 54px; width: 304px; height: 174px; box-shadow: 0 3px 8px rgba(0,0,0,.25); }
  .card-front { top: 136px; background: var(--paper); overflow: hidden; }
  .card-front .band { position: absolute; left: 14px; top: 0; width: 27px; height: 100%; background: var(--slate); }
  .card-front .band-top { position: absolute; left: 14px; top: 0; width: 27px; height: 48px; background: var(--teal); }
  .card-front .brand { position: absolute; left: 50px; top: 26px; font-family: "Lato", sans-serif; font-weight: 900; font-size: 16px; color: var(--teal); letter-spacing: .3px; line-height: 1.05; }
  .card-front .person { position: absolute; left: 52px; top: 76px; font-family: "Lato", sans-serif; }
  .card-front .name { font-weight: 900; font-size: 10px; color: var(--teal); letter-spacing: .4px; }
  .card-front .title { font-size: 7px; color: var(--slate); margin-top: 1px; }
  .card-front .contact { position: absolute; left: 52px; top: 104px; font-family: "Lato", sans-serif; font-size: 7px; color: var(--teal); line-height: 9px; }
  .contact-line { display: flex; align-items: center; gap: 3px; }
  .contact-line svg { width: 6px; height: 6px; fill: var(--slate); }
  .card-front .address { position: absolute; left: 52px; top: 128px; font-family: "Lato", sans-serif; font-size: 7px; color: var(--teal); line-height: 9px; }

  .card-back { top: 337px; background: linear-gradient(160deg, #3f5063, #344455); display: flex; align-items: center; justify-content: center; }
  .card-back .brand { font-family: "Lato", sans-serif; font-weight: 900; font-size: 24px; color: #fff; text-align: center; line-height: 1.05; letter-spacing: .5px; }

  .letterhead { position: absolute; left: 401px; top: 122px; width: 736px; height: 952px; background: var(--paper); box-shadow: 0 3px 10px rgba(0,0,0,.25); overflow: hidden; }
  .letterhead .band { position: absolute; left: 12px; top: 0; width: 58px; height: 100%; background: var(--slate); }
  .letterhead .band-top { position: absolute; left: 12px; top: 0; width: 58px; height: 82px; background: var(--teal); }
  .letterhead .brand { position: absolute; left: 87px; top: 48px; font-family: "Lato", sans-serif; font-weight: 900; font-size: 36px; color: var(--teal); letter-spacing: .5px; line-height: 1.02; }

  .letter { position: absolute; left: 109px; top: 214px; width: 576px; font-size: 12px; color: var(--ink); line-height: 16.8px; hyphens: auto; -webkit-hyphens: auto; }
  .letter .date { margin-bottom: 16px; }
  .letter .recipient { margin-bottom: 33px; }
  .letter strong { font-weight: 700; }
  .letter .salutation { margin-bottom: 16px; }
  .letter p { margin-bottom: 16px; text-align: left; }
  .letter .closing { margin-top: 34px; }
  .signature { width: 255px; height: 34px; margin: 4px 0 6px -10px; background: linear-gradient(90deg, var(--signature), rgba(220,220,220,.2)); border-radius: 4px; }

  .letter-footer { position: absolute; left: 109px; top: 888px; display: flex; font-family: "Lato", sans-serif; font-size: 12.5px; color: var(--teal); line-height: 14.5px; }
  .letter-footer .address { padding-right: 14px; border-right: 1px solid var(--teal); }
  .letter-footer .phones { padding-left: 18px; padding-top: 14px; }
  .letter-footer .contact-line { gap: 5px; }
  .letter-footer .contact-line svg { width: 8px; height: 8px; }
</style>
</head>
<body>
  <svg width="0" height="0" style="position:absolute">
    <symbol id="icon-phone" viewBox="0 0 10 10"><path d="M2 0.5 L3.8 2.6 L2.9 3.8 Q4.2 6 6.2 7.1 L7.4 6.2 L9.5 8 L8.3 9.5 Q1 8 0.5 1.7 Z"/></symbol>
    <symbol id="icon-fax" viewBox="0 0 10 10"><rect x="2.5" y="0.5" width="5" height="3"/><rect x="0.5" y="3.5" width="9" height="4" rx="1"/><rect x="2.5" y="7" width="5" height="2.5"/></symbol>
  </svg>

  <section class="card card-front" aria-label="Business card front">
    <div class="band"></div>
    <div class="band-top"></div>
    <div class="brand">CEDAR RIDGE</div>
    <div class="person">
      <div class="name">TRAVIS LUNDQOR</div>
      <div class="title">CMCA</div>
    </div>
    <div class="contact">
      <div class="contact-line"><svg><use href="#icon-phone"/></svg>555-237-4190</div>
      <div class="contact-line"><svg><use href="#icon-fax"/></svg>555-237-8856</div>
    </div>
    <div class="address">
      Cedar Ridge Property Group LLC<br>
      812 NE Tamber Ln.<br>
      Suite 9, Alderton, Nevada, 97815
    </div>
  </section>

  <section class="card card-back" aria-label="Business card back">
    <div class="brand">CEDAR RIDGE</div>
  </section>

  <section class="letterhead" aria-label="Letterhead">
    <div class="band"></div>
    <div class="band-top"></div>
    <div class="brand">CEDAR RIDGE</div>

    <div class="letter">
      <div class="date">January 1, 2050</div>
      <div class="recipient">
        <strong>Daniel Harrow</strong><br>
        Managing Director<br>
        Co.Street, Building/Suite<br>
        City/State, Zip Code
      </div>
      <div class="salutation">Dear Owen Callister,</div>
      <p>Lorem ipsum dolor sit amet, consectetuer adipiscing elit, sed diam nonummy nibh euismod tincidunt ut laoreet dolore magna aliquam erat volutpat. Ut wisi enim ad minim veniam, quis nostrud exerci tation ullamcorper suscipit lobortis nisl ut aliquip ex ea commodo consequat. Duis dolore te feugait nulla facilisi. Nam liber tempor cum soluta nobis eleifend option congue nihil imperdiet doming id quod mazim placerat facer possim assum. Lorem ipsum dolor sit amet, consectetuer adipiscing elit, sed diam nonummy nibh euismod tincidunt ut laoreet dolore magna aliquam erat volutpat. Ut wisi enim ad minim veniam, quis nostrud exerci tation ullamcorper suscipit lobortis nisl ut aliquip ex ea commodo consequat.</p>
      <p>Consectetuer adipiscing elit, sed diam nonummy nibh euismod tincidunt ut laoreet dolore magna aliquam erat volutpat. Ut wisi enim ad minim veniam, quis nostrud exerci tation ullamcorper suscipit lobortis nisl ut aliquip ex ea commodo consequat. Consectetuer adipiscing elit, sed diam nonummy nibh euismod tincidunt ut laoreet dolore magna aliquam erat volutpat. Ut wisi enim ad minim veniam, quis nostrud exerci tation ullamcorper suscipit lobortis nisl ut aliquip ex ea commodo consequat.</p>
      <p>Duis dolore te feugait nulla facilisi. Nam liber tempor cum soluta nobis eleifend option congue nihil imperdiet doming id quod mazim placerat facer possim assum.Duis dolore te feugait nulla facilisi. Nam liber tempor cum soluta nobis eleifend option congue nihil imperdiet doming id quod mazim placerat facer possim assum.</p>
      <div class="closing">Sincerely Yours,</div>
      <div class="signature" role="img" aria-label="Handwritten signature of Marcus Ellery"></div>
      <div><strong>Authorized Managing Director</strong><br>Company Name Here</div>
    </div>

    <footer class="letter-footer">
      <div class="address">
        Cedar Ridge Property Group LLC<br>
        812 NE Tamber Ln.<br>
        Suite 9, Alderton, Nevada, 97815
      </div>
      <div class="phones">
        <div class="contact-line"><svg><use href="#icon-phone"/></svg>555-237-4190</div>
        <div class="contact-line"><svg><use href="#icon-fax"/></svg>555-237-8856</div>
      </div>
    </footer>
  </section>
</body>
</html>
```